Corrow Family Farm fresh honey jar label

I need a label for jars of honey harvested at our farm. These are for gifts and personal use. We are looking to incorporate our farm brand into the label. We would like the design to take the existing brand and add some element like bees, honey, flowers, or hives to indicate the contents. We want the design to feel homemade and authentic without feeling cheap or hoaky

Requirements
Must have
• The label must be made to fit a 1" x2" rectangular label. The label must include the attached family brand. The label must include the text "Corrow Family Farms" "Pinebrook, USA" "Farm Fresh Honey". The label will be printed on off-white paper
Nice to have
• It would be nice to have illustrations of bees or flowers around the logo or hives or honeycombs. The label should have a vintage feel
Should not have
• The label should not feel overly cartoonish or hoaky

```html
<!DOCTYPE html>
<html lang="en">
<head>
<meta charset="utf-8">
<title>Corrow Family Farms – Farm Fresh Honey Label</title>
<link href="https://fonts.googleapis.com/css2?family=Bubblegum+Sans&display=swap" rel="stylesheet">
<style>
  :root {
    --page: #efefef;
    --label-paper: #ffffff;
    --etching-light: #f1f1f1;
    --etching-mid: #dcdcdc;
    --honey-gold: #c9920e;
    --ink-light: #ffffff;
  }
  * { margin: 0; padding: 0; box-sizing: border-box; }
  html, body {
    width: 846px;
    height: 1200px;
    overflow: hidden;
    background: var(--page);
  }
  .canvas {
    position: relative;
    width: 846px;
    height: 1200px;
    display: flex;
    align-items: center;
    justify-content: center;
  }
  .honey-label {
    position: relative;
    width: 720px;
    height: 360px;
    background: var(--label-paper);
    overflow: hidden;
    font-family: "Bubblegum Sans", "Trebuchet MS", sans-serif;
    color: var(--ink-light);
  }
  .floral-etching {
    position: absolute;
    inset: 0;
    background:
      radial-gradient(circle at 12% 22%, var(--etching-mid) 0, transparent 22%),
      radial-gradient(circle at 10% 82%, var(--etching-mid) 0, transparent 20%),
      radial-gradient(circle at 88% 20%, var(--etching-mid) 0, transparent 22%),
      radial-gradient(circle at 92% 78%, var(--etching-mid) 0, transparent 22%),
      radial-gradient(circle at 40% 10%, var(--etching-mid) 0, transparent 16%),
      linear-gradient(var(--etching-light), var(--etching-light));
  }
  .badge {
    position: absolute;
    inset: 0;
    width: 720px;
    height: 360px;
  }
  .badge-shape { fill: var(--honey-gold); }
  .brand-mark {
    position: absolute;
    left: 272px;
    width: 177px;
    top: 58px;
    text-align: center;
    font-size: 34px;
    letter-spacing: 2px;
    line-height: 1;
  }
  .label-text {
    position: absolute;
    left: 108px;
    width: 497px;
    top: 150px;
    text-align: center;
    text-transform: uppercase;
  }
  .farm-name {
    font-size: 46px;
    line-height: 1;
    letter-spacing: 1px;
  }
  .product-name {
    margin-top: 8px;
    font-size: 27px;
    line-height: 1;
    letter-spacing: 1px;
  }
  .origin {
    margin-top: 22px;
    font-size: 13px;
    line-height: 1;
    letter-spacing: 1px;
  }
</style>
</head>
<body>
  <main class="canvas">
    <section class="honey-label">
      <div class="floral-etching" role="img" aria-label="Grey etched illustration of bees, blossoms and leaves covering the label background"></div>
      <svg class="badge" viewBox="0 0 720 360" aria-hidden="true">
        <path class="badge-shape"
          d="M138 104 H272 A88.5 88.5 0 0 1 449 104 H575 A30 30 0 0 1 605 134 V283 A30 30 0 0 1 575 313 H138 A30 30 0 0 1 108 283 V134 A30 30 0 0 1 138 104 Z"/>
      </svg>
      <div class="brand-mark">CORROW</div>
      <div class="label-text">
        <h1 class="farm-name">Corrow Family Farms</h1>
        <p class="product-name">Farm Fresh Honey</p>
        <p class="origin">Pinebrook, USA</p>
      </div>
    </section>
  </main>
</body>
</html>
```